Need a Marketing System Program Overview Flyer

Our business, Builder Momentum Network, helps General Contractors and home improvement businesses to generate high quality leads, acquire new customers, and improve their overall online presence.

The system includes a...
- High Converting Website
- SEO & Online Listings Management
- Strategic PPC Advertising
- Email Marketing and Automation
- Social Media Management & Retargeting Campaigns
- Reputation Management
- Tracking and Reporting

The Brochure or flyer needs to have a very professional and high class look that wows the potential customers when overviewing the program.

It needs to give a clear explanation of the program while simultaneously having the very best design concept that pulls the reader in.

I've attached our branding guide, logos and additional information...

Our site is currently being staged at www.ridgevantix.com/BMN

```html
<!DOCTYPE html>
<html lang="en">
<head>
<meta charset="utf-8">
<title>Builder Momentum Network – Program Flyer</title>
<link href="https://fonts.googleapis.com/css2?family=Oswald:wght@400;500;600;700&family=Open+Sans:wght@400;600;700&display=swap" rel="stylesheet">
<style>
  :root{
    --gold:#b8a06a;
    --ink:#111111;
    --charcoal:#2b2b2b;
    --paper:#ffffff;
    --stage:#e4e2dd;
    --text:#2a2a2a;
  }
  *{box-sizing:border-box;margin:0;padding:0}
  html,body{width:1200px;height:900px;overflow:hidden;background:var(--stage)}
  body{font-family:"Open Sans",Arial,sans-serif;color:var(--text);position:relative}

  .sheet{position:absolute;top:82px;width:560px;height:736px;background:var(--paper);overflow:hidden;box-shadow:0 6px 22px rgba(0,0,0,.18)}
  .sheet--intro{left:26px}
  .sheet--system{left:614px}

  /* ---------- intro sheet ---------- */
  .intro-hero{position:absolute;left:0;top:0;width:560px;height:230px;background:var(--gold)}
  .intro-hero__corner{position:absolute;right:0;top:0}
  .intro-hero__question{position:absolute;left:30px;top:30px;width:300px;font-size:16px;line-height:1.3;color:#fff}
  .intro-hero__question b{font-weight:700}
  .intro-hero__cta{position:absolute;left:30px;top:158px;background:var(--ink);color:#fff;padding:7px 16px;font-size:13.5px;line-height:1.25;border:2px solid #fff}
  .intro-hero__cta b{font-weight:700;text-transform:uppercase}
  .checklist-art{position:absolute;left:338px;top:22px;width:196px;height:180px;border-radius:4px;background:linear-gradient(160deg,#fafafa,#d9d3c3)}

  .mission{position:absolute;left:0;top:230px;width:560px;height:92px;background:var(--charcoal);color:#fff;text-align:center;font-size:12.5px;font-weight:700;line-height:1.5;padding:16px 28px 0}
  .howto{position:absolute;left:150px;top:306px;background:var(--gold);color:#fff;font-weight:700;font-size:22px;padding:3px 34px;clip-path:polygon(6% 0,100% 0,94% 100%,0 100%)}

  .steps{position:absolute;left:24px;top:356px;width:326px}
  .step{display:flex;gap:14px;height:80px;margin-bottom:4px}
  .step__art{flex:0 0 78px;height:72px;border-radius:4px;background:linear-gradient(150deg,#f1e6c8,#c9ab64)}
  .step__body{border-left:2px solid var(--gold);padding-left:12px}
  .step__title{font-size:14px;line-height:1.2;color:var(--ink);margin-bottom:3px}
  .step__text{font-size:9.5px;line-height:1.35;color:#333}
  .portrait{position:absolute;left:358px;top:340px;width:202px;height:344px;background:linear-gradient(180deg,#d9d6d0 0%,#3a3f45 55%,#1d2228 100%)}

  .ready{position:absolute;left:24px;top:622px;white-space:nowrap;border:1.5px solid var(--ink);background:#fff;padding:4px 12px;font-family:"Oswald",Arial,sans-serif;font-size:13px;font-weight:600;color:var(--ink);text-transform:uppercase}
  .ready span{color:var(--gold)}

  .footer{position:absolute;left:0;bottom:0;width:560px;height:52px}
  .footer__start{position:absolute;left:0;top:0;width:230px;height:52px;background:var(--gold);color:var(--ink);font-weight:700;font-size:17px;display:flex;align-items:center;padding-left:34px;clip-path:polygon(0 0,88% 0,100% 100%,0 100%)}
  .footer__contact{position:absolute;left:210px;top:0;right:0;height:52px;background:var(--ink);color:var(--gold);display:flex;align-items:center;gap:16px;padding-left:36px;font-size:16px;font-weight:600;clip-path:polygon(0 0,100% 0,100% 100%,6% 100%)}
  .footer__contact svg{vertical-align:-3px;margin-right:6px}

  /* ---------- system sheet ---------- */
  .brandbar{position:absolute;left:0;top:0;width:560px;height:130px;background:#fff}
  .brandbar__tab{position:absolute;right:0;top:0;width:240px;height:70px;background:var(--gold);clip-path:polygon(14% 0,100% 0,100% 100%,0 100%)}
  .brandbar__url{position:absolute;right:22px;top:40px;color:#fff;font-size:11px;font-weight:600}
  .brand{position:absolute;left:34px;top:70px;display:flex;align-items:center;gap:10px}
  .brand__mark{width:16px;height:16px;background:var(--ink)}
  .brand__name{font-family:"Oswald",Arial,sans-serif;font-size:24px;font-weight:600;color:var(--ink);text-transform:uppercase;letter-spacing:.5px}

  .hero{position:absolute;left:0;top:130px;width:560px;height:290px;background:var(--ink)}
  .hero__coins{position:absolute;right:0;top:0;width:250px;height:290px;background:radial-gradient(ellipse at 60% 70%,#8a7337 0%,#3d3219 45%,#111 80%)}
  .hero__title{position:absolute;left:32px;top:38px;font-family:"Oswald",Arial,sans-serif;color:#fff;text-transform:uppercase;line-height:1.1}
  .hero__l1{font-size:24px;font-weight:500}
  .hero__l1 b{font-weight:700}
  .hero__l2{font-size:40px;font-weight:700;color:var(--gold)}
  .hero__l3{font-size:24px;font-weight:500}
  .hero__l3 b{font-weight:700}
  .hero__l4{display:inline-block;margin-top:8px;background:var(--gold);color:var(--ink);font-size:36px;font-weight:700;padding:0 14px}

  .promise{position:absolute;left:0;top:420px;width:560px;height:44px;background:var(--gold);text-align:center;font-family:"Oswald",Arial,sans-serif;font-weight:600;color:#fff;font-size:16px;text-transform:uppercase;padding-top:6px}
  .promise__roi{position:absolute;left:50%;transform:translateX(-50%);top:452px;white-space:nowrap;background:var(--ink);color:#fff;font-family:"Oswald",Arial,sans-serif;font-weight:600;font-size:17px;text-transform:uppercase;padding:3px 22px}

  .services{position:absolute;left:20px;top:502px;width:520px;display:grid;grid-template-columns:repeat(4,1fr);row-gap:12px}
  .service{text-align:center;font-size:10.5px;line-height:1.3;color:var(--ink)}
  .service__dot{width:40px;height:40px;margin:0 auto 5px;border-radius:50%;background:var(--gold);border:3px solid #f4ecd8;box-shadow:0 2px 4px rgba(0,0,0,.2)}
</style>
</head>
<body>

<section class="sheet sheet--intro">
  <div class="intro-hero">
    <svg class="intro-hero__corner" width="260" height="230" viewBox="0 0 260 230"><polygon points="60,0 260,0 260,230 0,230" fill="#f2f2f2"/></svg>
    <p class="intro-hero__question">Does your <b>Business Struggle with Building a Steady Flow of qualified leads</b> using outdated marketing methods that <b>Just don't work?</b></p>
    <p class="intro-hero__cta">Take The Perfect First Step<br><b>to grow your business.</b></p>
    <div class="checklist-art" role="img" aria-label="Spiral-bound marketing checklist booklet with a cartoon builder and sample checklist pages"></div>
  </div>

  <p class="mission">We Help General Contractors Implement A Results-Driven Online Marketing System That Is Proven To Generate The Highest-Quality Leads, Convert Those Leads Into Customers, And Ultimately... Increase Your Revenue.</p>
  <h2 class="howto">How Do We Do It?</h2>

  <div class="steps">
    <div class="step">
      <div class="step__art" role="img" aria-label="Funnel illustration with leads leaking out"></div>
      <div class="step__body">
        <h3 class="step__title">Analyze Where Your Funnel/Website Is Leaking Customers</h3>
        <p class="step__text">We Take A Deep Dive Into Your Current Marketing System, Website And Process.</p>
      </div>
    </div>
    <div class="step">
      <div class="step__art" role="img" aria-label="Stacked blueprint report pages"></div>
      <div class="step__body">
        <h3 class="step__title">Get A Customized Marketing Blueprint</h3>
        <p class="step__text">We Work With You To Make Sure You Understand The Key Things You'll Need To Do To Achieve Your Business Goals.</p>
      </div>
    </div>
    <div class="step">
      <div class="step__art" role="img" aria-label="Magnet and funnel drawing in a crowd of workers"></div>
      <div class="step__body">
        <h3 class="step__title">Take Your Business To The Next Level</h3>
        <p class="step__text">We Implement The Blueprint To Generate More Revenue With An Online Marketing &amp; Lead Generation System</p>
      </div>
    </div>
  </div>

  <div class="portrait" role="img" aria-label="Portrait of the program consultant in a dark polo shirt, arms crossed"></div>

  <p class="ready">Are you ready <span>to build and grow your business?</span></p>

  <footer class="footer">
    <div class="footer__start">GET STARTED NOW</div>
    <div class="footer__contact">
      <span><svg width="16" height="16" viewBox="0 0 16 16"><circle cx="8" cy="8" r="7" fill="none" stroke="#fff" stroke-width="1.4"/><path d="M5.5 4.5l1.5 1.5-1 1c.6 1.2 1.4 2 2.6 2.6l1-1 1.5 1.5-1 1c-2.7-.5-4.9-2.7-5.4-5.4z" fill="#fff"/></svg>(555) 014-2290</span>
      <span><svg width="16" height="12" viewBox="0 0 16 12"><rect x=".7" y=".7" width="14.6" height="10.6" fill="none" stroke="#fff" stroke-width="1.3"/><path d="M1 1l7 6 7-6" fill="none" stroke="#fff" stroke-width="1.3"/></svg>info@bmn.com</span>
    </div>
  </footer>
</section>

<section class="sheet sheet--system">
  <header class="brandbar">
    <div class="brandbar__tab"></div>
    <span class="brandbar__url">www.ridgevantix.com/BMN</span>
    <div class="brand"><span class="brand__mark"></span><span class="brand__name">Builder Momentum Network</span></div>
  </header>

  <div class="hero">
    <div class="hero__coins" role="img" aria-label="Stacks of gold coins rising like stairs with miniature construction workers"></div>
    <h1 class="hero__title">
      <div class="hero__l1"><b>Accelerate</b> your</div>
      <div class="hero__l2">Lead Generation</div>
      <div class="hero__l3">While <b>increasing sales</b> and</div>
      <div class="hero__l4">Reducing Costs</div>
    </h1>
  </div>

  <div class="promise">Our 8-point Builder Momentum Network will show you what</div>
  <div class="promise__roi">Return on investment truly means!</div>

  <div class="services">
    <div class="service"><div class="service__dot"></div>High Converting<br>Website</div>
    <div class="service"><div class="service__dot"></div>SEO &amp; Online<br>Listings Management</div>
    <div class="service"><div class="service__dot"></div>Strategic<br>PPC Advertising</div>
    <div class="service"><div class="service__dot"></div>Email Marketing<br>and Automation</div>
    <div class="service"><div class="service__dot"></div>Social Media<br>Management</div>
    <div class="service"><div class="service__dot"></div>Retargeting<br>Campaigns</div>
    <div class="service"><div class="service__dot"></div>Reputation<br>Management</div>
    <div class="service"><div class="service__dot"></div>Tracking<br>and Reporting</div>
  </div>

  <footer class="footer">
    <div class="footer__start">GET STARTED NOW</div>
    <div class="footer__contact">
      <span><svg width="16" height="16" viewBox="0 0 16 16"><circle cx="8" cy="8" r="7" fill="none" stroke="#fff" stroke-width="1.4"/><path d="M5.5 4.5l1.5 1.5-1 1c.6 1.2 1.4 2 2.6 2.6l1-1 1.5 1.5-1 1c-2.7-.5-4.9-2.7-5.4-5.4z" fill="#fff"/></svg>(555) 014-2290</span>
      <span><svg width="16" height="12" viewBox="0 0 16 12"><rect x=".7" y=".7" width="14.6" height="10.6" fill="none" stroke="#fff" stroke-width="1.3"/><path d="M1 1l7 6 7-6" fill="none" stroke="#fff" stroke-width="1.3"/></svg>info@bmn.com</span>
    </div>
  </footer>
</section>

</body>
</html>
```